Escrow Accounting firm needs a website design for a startup that services clients nationally.

I offer escrow accounting services for title companies and real estate attorneys. I've enclosed a logo, color palette and flyers with content that can be used for the site.

I'm looking for a similar design concept as the website below from my former employer. Please don't copy because of copyright infringement. Including for design ideas only.
www.harborlineaccounting.com

Below is a brief write-up...
For professionals in the title insurance industry, finding a trustworthy and budget-friendly solution for escrow accounting can be daunting. When choosing the right accounting partner, title companies and law firms need a group they can rely on, and that's where we come in.

```html
<!DOCTYPE html>
<html lang="en">
<head>
<meta charset="UTF-8">
<title>Meridian Escrow Solutions</title>
<link href="https://fonts.googleapis.com/css2?family=Outfit:wght@300;400;500;600&display=swap" rel="stylesheet">
<style>
:root{
  --navy:#2b3341;
  --slate:#3b4558;
  --clay:#bf6f58;
  --clay-soft:#c9826c;
  --ink:#2f3644;
  --text:#5a5f69;
  --line:#d7d9de;
  --white:#ffffff;
}
*{box-sizing:border-box;margin:0;padding:0}
html,body{width:1200px;height:4542px;overflow:hidden}
body{font-family:"Outfit",sans-serif;color:var(--text);background:var(--white);position:relative}
.abs{position:absolute}
.label{font-size:12px;letter-spacing:1.5px;text-transform:uppercase;color:var(--clay);border-bottom:1px solid var(--clay);padding-bottom:3px;display:inline-block}
.h2{font-size:38px;font-weight:500;color:var(--ink);text-transform:uppercase;letter-spacing:.5px}
.btn{display:flex;align-items:center;justify-content:center;font-size:11px;border-radius:4px}
.btn-clay{background:var(--clay);color:var(--white)}
.btn-outline{border:1px solid var(--ink);color:var(--ink)}
.photo{background:linear-gradient(135deg,#b9a698,#6e6258)}

.topbar{top:0;left:0;width:1200px;height:32px;background:var(--navy)}
.social{display:flex;gap:5px}
.social span{width:12px;height:12px;border-radius:50%;background:var(--white)}
.social.orange span{background:var(--clay-soft)}

.nav{top:32px;left:0;width:1200px;height:60px;display:flex;align-items:center}
.logo{display:flex;align-items:center;gap:8px;color:var(--clay);font-size:22px;font-weight:500;line-height:1}
.logo small{display:block;font-size:8px;letter-spacing:1.5px;color:var(--ink)}
.logo i{width:22px;height:22px;border:2px solid var(--clay);display:block}
.menu{display:flex;gap:32px;font-size:11px;color:var(--ink)}
.menu .on{color:var(--clay)}

.hero{top:92px;left:0;width:1200px;height:599px;background:linear-gradient(90deg,#2e2a28 0%,#4a4440 45%,#8a7a6e 100%)}
.hero h1{font-size:50px;font-weight:500;color:var(--white);line-height:62px;text-transform:uppercase}

.about p{font-size:11px;line-height:17px;color:var(--text);margin-bottom:12px}

.features{top:1218px;left:0;width:1200px;height:255px;background:var(--navy);display:flex;padding:36px 122px 0}
.feat{flex:1;text-align:center;color:var(--white);padding:0 40px;border-right:1px solid #4d5667;height:170px}
.feat:last-child{border-right:none}
.feat h3{font-size:15px;font-weight:500;margin:14px 0 12px}
.feat p{font-size:9.5px;line-height:15px;color:#c6cad2}

.svc{top:1662px;width:224px;height:227px;border:1px solid #b8bcc4;border-radius:8px;text-align:center;padding:18px 14px}
.svc .ic{width:56px;height:56px;border-radius:50%;background:var(--clay);margin:0 auto 14px;display:flex;align-items:center;justify-content:center}
.svc h3{font-size:14px;font-weight:500;color:var(--ink);margin-bottom:12px}
.svc p{font-size:9.5px;line-height:15px}
.svc a{display:inline-block;margin-top:14px;font-size:11px;color:var(--clay);text-decoration:underline;letter-spacing:1px}
.svc.active{background:var(--clay);border-color:var(--clay)}
.svc.active h3,.svc.active p,.svc.active a{color:var(--white)}
.svc.active .ic{background:var(--white)}

.why{top:2009px;left:0;width:1200px;height:610px;background:var(--slate)}
.why-list{top:63px;left:597px;width:480px;height:487px;border:1px solid #c9ccd3;border-radius:8px}
.why-item{height:162px;border-bottom:1px solid #c9ccd3;padding:30px 30px 0;position:relative;color:var(--white)}
.why-item:last-child{border-bottom:none}
.why-item .num{position:absolute;top:14px;left:28px;font-size:46px;color:transparent;-webkit-text-stroke:1px #6c7588;font-weight:500}
.why-item h3{position:relative;font-size:18px;font-weight:400;margin-top:38px;margin-bottom:14px}
.why-item p{position:relative;font-size:10px;line-height:17px;color:#d4d7dd}

.tcard{top:2810px;width:306px;height:233px;border:1px solid var(--line);border-radius:8px;padding:20px 18px}
.tcard h4{font-size:14px;font-weight:500;color:var(--ink)}
.stars{color:#f0a92e;font-size:12px;letter-spacing:2px;margin:6px 0 8px}
.tcard p{font-size:10px;line-height:18px}
.tcard .who{margin-top:18px;font-size:12px;color:var(--clay)}
.tcard .role{font-size:9px;color:var(--ink)}
.tcard .q{position:absolute;right:18px;bottom:24px;font-size:52px;line-height:30px;color:var(--clay);font-weight:600}
.arrow{top:2910px;width:36px;height:36px;border:1px solid #9aa0aa;border-radius:50%;display:flex;align-items:center;justify-content:center}

.blog{top:3101px;left:0;width:1200px;height:599px;background:var(--navy)}
.post-img{top:168px;width:467px;height:268px;border-radius:6px}
.tag{position:absolute;left:18px;bottom:14px;background:var(--clay);color:var(--white);font-size:9px;padding:6px 18px;border-radius:4px}
.post h3{font-size:18px;font-weight:400;color:var(--white);line-height:24px;width:420px}
.post a{display:inline-block;margin-top:10px;font-size:11px;color:#d4d7dd;text-decoration:underline;letter-spacing:1px}

.field{border:1px solid #b9bcc3;border-radius:3px;font-size:9px;color:#9a9ea6;padding:12px 16px}

.footer{top:4215px;left:0;width:1200px;height:327px;background:var(--slate);color:var(--white)}
.footer h4{font-size:13px;font-weight:500;margin-bottom:14px}
.flinks{font-size:10px;line-height:26px;color:#d4d7dd}
.crow{display:flex;align-items:center;gap:14px;font-size:11px;color:#d4d7dd;margin-bottom:14px;line-height:16px}
.crow i{width:24px;height:24px;border-radius:50%;background:var(--white);display:flex;align-items:center;justify-content:center;flex:none}
</style>
</head>
<body>

<div class="abs topbar">
  <div class="abs social" style="left:122px;top:10px"><span></span><span></span><span></span><span></span></div>
  <div class="abs social orange" style="left:1021px;top:10px"><span></span><span></span><span></span></div>
</div>

<header class="abs nav">
  <div class="abs logo" style="left:122px;top:14px"><i></i><div>MERIDIAN<small>ESCROW SOLUTIONS</small></div></div>
  <nav class="abs menu" style="left:433px;top:26px">
    <span class="on">Home</span><span>About Us</span><span>Services</span><span>Testimonials</span><span>Resources</span>
  </nav>
  <div class="abs btn btn-clay" style="left:840px;top:16px;width:111px;height:29px">Contact Us</div>
  <div class="abs btn btn-outline" style="left:960px;top:16px;width:117px;height:29px">Get In Touch</div>
</header>

<section class="abs hero" role="img" aria-label="Photo of a smiling couple reviewing documents with an advisor">
  <div class="abs" style="left:122px;top:134px;font-size:12px;letter-spacing:1.5px;color:var(--white);border-bottom:1px solid var(--white);padding-bottom:3px">WELCOME TO MERIDIAN ESCROW SOLUTION</div>
  <h1 class="abs" style="left:122px;top:180px">Secure, Compliant,<br>and Efficient<br>Escrow Solutions</h1>
  <p class="abs" style="left:122px;top:392px;font-size:12px;color:var(--white)">Customized Solutions for Title Companies and Real Estate Attorneys</p>
  <div class="abs btn btn-clay" style="left:122px;top:435px;width:169px;height:28px">Get a Free Consultation</div>
</section>

<section class="about">
  <div class="abs photo" style="left:122px;top:747px;width:317px;height:266px;border-radius:6px" role="img" aria-label="Portrait of a smiling professional woman"></div>
  <div class="abs photo" style="left:310px;top:895px;width:319px;height:265px;border-radius:10px;border:4px solid var(--white);background:linear-gradient(135deg,#d9d6d2,#8d8680)" role="img" aria-label="Hands passing house keys over a desk">
    <svg class="abs" style="left:138px;top:112px" width="40" height="40" viewBox="0 0 40 40"><circle cx="20" cy="20" r="20" fill="#bf6f58"/><path d="M16 13l11 7-11 7z" fill="#fff"/></svg>
  </div>
  <div class="abs label" style="left:682px;top:776px">About Us on Meridian Escrow Solution</div>
  <h2 class="abs h2" style="left:682px;top:814px">Who We Are</h2>
  <div class="abs" style="left:682px;top:866px;width:390px">
    <p>Meridian Escrow Solutions has accounting experts who understand the title industry and the importance of compliance, security, and implementing precise escrow accounting procedures along with timely monthly reporting.</p>
    <p>With years of experience in the title industry, our team of accounting experts understands the importance of compliance, security, and precision. We are dedicated to implementing rigorous escrow accounting procedures that align with recognized industry best practices, ensuring that your financials are always audit-ready.</p>
    <p>At Meridian Escrow Solutions, we pride ourselves on our integrity, efficiency, and commitment to our clients' success. We understand the challenges you face in the title insurance industry, and we're here to be the reliable partner you can trust with your escrow accounting needs.</p>
  </div>
  <div class="abs btn btn-outline" style="left:682px;top:1105px;width:111px;height:28px">Learn More</div>
</section>

<section class="abs features">
  <div class="feat">
    <svg width="50" height="52" viewBox="0 0 50 52" fill="none" stroke="#fff" stroke-width="1.5"><circle cx="20" cy="22" r="6"/><path d="M8 46c0-8 5-13 12-13s12 5 12 13"/><path d="M30 38h10v8H30z"/><path d="M14 6l2 3M25 4v4M36 6l-2 3" stroke="#bf6f58"/></svg>
    <h3>Expertise in Title Insurance</h3>
    <p>With years of specialized experience, we understand the complexities of the title insurance industry and are committed to providing precise escrow accounting solutions</p>
  </div>
  <div class="feat">
    <svg width="50" height="52" viewBox="0 0 50 52" fill="none" stroke="#fff" stroke-width="1.5"><path d="M18 36c-6-4-8-9-8-14a12 12 0 0124 0c0 5-2 10-8 14z"/><path d="M18 40h8M19 44h6"/><circle cx="34" cy="40" r="8" stroke="#bf6f58"/><path d="M34 36v8" stroke="#bf6f58"/></svg>
    <h3>Cost-Effective Solutions</h3>
    <p>Our services are tailored to your needs, offering you comprehensive solutions at competitive rates, ensuring you get the best value for your investment</p>
  </div>
  <div class="feat">
    <svg width="50" height="52" viewBox="0 0 50 52" fill="none" stroke="#fff" stroke-width="1.5"><path d="M25 4l10 4v9c0 6-4 10-10 12-6-2-10-6-10-12V8z" stroke="#bf6f58"/><path d="M4 36l10-6 8 4 6-2 8 4 10-2M14 40l6 6 6-4 6 4 6-6"/></svg>
    <h3>Trusted by Professionals</h3>
    <p>We're proud to be the trusted choice for title companies and real estate attorneys, delivering reliable, secure, and compliant services that professionals rely on</p>
  </div>
</section>

<section>
  <div class="abs label" style="left:0;width:1200px;text-align:center;top:1527px;border:none"><span style="border-bottom:1px solid var(--clay);padding-bottom:3px">Our Service</span></div>
  <h2 class="abs h2" style="left:0;width:1200px;text-align:center;top:1558px">What We Do</h2>
  <p class="abs" style="left:0;width:1200px;text-align:center;top:1622px;font-size:11px;color:var(--ink)">Comprehensive Escrow Accounting Solutions Tailored to Your Needs</p>

  <div class="abs svc" style="left:122px">
    <div class="ic"><svg width="28" height="28" viewBox="0 0 28 28" fill="none" stroke="#fff" stroke-width="1.5"><circle cx="14" cy="14" r="10"/><path d="M14 8v12M10 11h6a2 2 0 010 4h-4a2 2 0 000 4h6"/></svg></div>
    <h3>Escrow Reconciliation</h3>
    <p>Ensure accuracy and compliance with our meticulous daily and monthly escrow reconciliation services. We meticulously compare and verify your financial records to maintain integrity and transparency.</p>
    <a>Learn More</a>
  </div>
  <div class="abs svc" style="left:365px">
    <div class="ic"><svg width="28" height="28" viewBox="0 0 28 28" fill="none" stroke="#fff" stroke-width="1.5"><rect x="6" y="4" width="16" height="20" rx="2"/><path d="M10 10h8M10 14h8M10 18h5"/></svg></div>
    <h3>Compliance Assurance</h3>
    <p>Ensure accuracy and compliance with our meticulous daily and monthly escrow reconciliation services. We meticulously compare and verify your financial records to maintain integrity and transparency.</p>
    <a>Learn More</a>
  </div>
  <div class="abs svc active" style="left:608px">
    <div class="ic"><svg width="28" height="28" viewBox="0 0 28 28" fill="none" stroke="#2f3644" stroke-width="1.5"><rect x="5" y="4" width="14" height="20" rx="2"/><path d="M9 10h6M9 14h6"/><circle cx="19" cy="19" r="4"/></svg></div>
    <h3>Customized Reporting</h3>
    <p>Ensure accuracy and compliance with our meticulous daily and monthly escrow reconciliation services. We meticulously compare and verify your financial records to maintain integrity and transparency.</p>
    <a>Learn More</a>
  </div>
  <div class="abs svc" style="left:853px">
    <div class="ic"><svg width="28" height="28" viewBox="0 0 28 28" fill="none" stroke="#fff" stroke-width="1.5"><rect x="4" y="5" width="10" height="8" rx="1"/><rect x="14" y="15" width="10" height="8" rx="1"/><path d="M9 13v6h5M19 15V9h-5"/></svg></div>
    <h3>Integration &amp; Support</h3>
    <p>Seamlessly integrate with all major accounting software systems through our expert support services. We ensure that your financial data flows smoothly and securely across platforms, enhancing.</p>
    <a>Learn More</a>
  </div>
  <div class="abs btn btn-outline" style="left:543px;top:1922px;width:112px;height:29px">Get In Touch</div>
</section>

<section class="abs why">
  <div class="abs label" style="left:122px;top:58px">Our Benefits</div>
  <h2 class="abs h2" style="left:122px;top:88px;color:var(--white)">Why Choose Us</h2>
  <p class="abs" style="left:122px;top:158px;width:310px;font-size:9.5px;line-height:15px;color:#d4d7dd">With years of specialized experience, we understand the complexities of the title insurance industry and are committed to providing precise escrow accounting solutions.</p>
  <div class="abs" style="left:122px;top:225px;width:415px;height:325px;border-radius:8px;background:linear-gradient(135deg,#e6d2b8,#8c6a4c)" role="img" aria-label="Hands placing a small model house on a desk"></div>
  <div class="abs why-list">
    <div class="why-item"><span class="num">01</span><h3>Lorem ipsum Dummy Text</h3><p>Our expert team is dedicated to providing precision and comfort in every waxing session. Trust us for a smooth, flawless experience every time.</p></div>
    <div class="why-item"><span class="num">02</span><h3>Lorem ipsum Dummy Text</h3><p>From meticulously sanitized equipment to impeccable cleanliness, your comfort and safety are our top priorities</p></div>
    <div class="why-item"><span class="num">03</span><h3>Lorem ipsum Dummy Text</h3><p>From meticulously sanitized equipment to impeccable cleanliness, your comfort and safety are our top priorities</p></div>
  </div>
</section>

<section>
  <div class="abs label" style="left:0;width:1200px;text-align:center;top:2678px;border:none"><span style="border-bottom:1px solid var(--clay);padding-bottom:3px">Testimonial</span></div>
  <h2 class="abs h2" style="left:0;width:1200px;text-align:center;top:2708px">What Our Clients Say</h2>
  <p class="abs" style="left:0;width:1200px;text-align:center;top:2771px;font-size:11px;color:var(--ink)">Lorem Ipsum is simply dummy text of the printing and typesetting industry.</p>
  <div class="abs arrow" style="left:65px"><svg width="14" height="10" viewBox="0 0 14 10" fill="none" stroke="#5a5f69" stroke-width="1.2"><path d="M13 5H1M5 1L1 5l4 4"/></svg></div>
  <div class="abs arrow" style="left:1096px"><svg width="14" height="10" viewBox="0 0 14 10" fill="none" stroke="#5a5f69" stroke-width="1.2"><path d="M1 5h12M9 1l4 4-4 4"/></svg></div>
  <div class="abs tcard" style="left:122px"><h4>Excelent Work</h4><div class="stars">★★★★★</div><p>Lorem Ipsum Is Simply Dummy Text Of The Printing And Typesetting Industry. Lorem Ipsum Has Been The Industry's Standard Dummy Text Ever Since 1500s. When An Unknown Printer Took A Galley Of Type And Scrambled It To Make A Type Specimen Book.</p><div class="who">Dana Reyes</div><div class="role">Client</div><span class="q">"</span></div>
  <div class="abs tcard" style="left:446px"><h4>Excelent Work</h4><div class="stars">★★★★★</div><p>Lorem Ipsum Is Simply Dummy Text Of The Printing And Typesetting Industry. Lorem Ipsum Has Been The Industry's Standard Dummy Text Ever Since 1500s. When An Unknown Printer Took A Galley Of Type And Scrambled It To Make A Type Specimen Book.</p><div class="who">Dana Reyes</div><div class="role">Client</div><span class="q">"</span></div>
  <div class="abs tcard" style="left:772px"><h4>Excelent Work</h4><div class="stars">★★★★★</div><p>Lorem Ipsum Is Simply Dummy Text Of The Printing And Typesetting Industry. Lorem Ipsum Has Been The Industry's Standard Dummy Text Ever Since 1500s. When An Unknown Printer Took A Galley Of Type And Scrambled It To Make A Type Specimen Book.</p><div class="who">Dana Reyes</div><div class="role">Client</div><span class="q">"</span></div>
</section>

<section class="abs blog">
  <div class="abs label" style="left:122px;top:58px">Our Resource</div>
  <h2 class="abs h2" style="left:122px;top:95px;color:var(--white)">Our Blog</h2>
  <div class="abs btn btn-clay" style="left:909px;top:104px;width:168px;height:30px">Get a Free Consultation</div>
  <div class="abs post-img" style="left:122px;background:linear-gradient(135deg,#e8e4de,#a49c92)" role="img" aria-label="Hands signing a document beside a model house"><span class="tag">20 may,2024 &nbsp; By Alex Moreno</span></div>
  <div class="abs post-img" style="left:611px;background:linear-gradient(135deg,#c7b29c,#5d6a80)" role="img" aria-label="Team meeting around a table"><span class="tag">20 may,2024 &nbsp; By Alex Moreno</span></div>
  <div class="abs post" style="left:122px;top:450px"><h3>Lorem Ipsum has been the industry's standard dummy text ever since the 1500s, when an unknown printer</h3><a>Learn More</a></div>
  <div class="abs post" style="left:611px;top:450px"><h3>Lorem Ipsum has been the industry's standard dummy text ever since the 1500s, when an unknown printer</h3><a>Learn More</a></div>
</section>

<section>
  <div class="abs" style="left:122px;top:3776px;width:356px;height:368px;border-radius:8px;background:linear-gradient(135deg,#c9a58a,#5a3e32)" role="img" aria-label="Support agent with a headset working at a laptop"></div>
  <div class="abs label" style="left:516px;top:3770px">Get In Touch</div>
  <h2 class="abs h2" style="left:516px;top:3808px">Contact Us</h2>
  <div class="abs field" style="left:516px;top:3882px;width:268px;height:36px">First Name</div>
  <div class="abs field" style="left:809px;top:3882px;width:268px;height:36px">Last Name</div>
  <div class="abs field" style="left:516px;top:3931px;width:268px;height:36px">Email</div>
  <div class="abs field" style="left:809px;top:3931px;width:268px;height:36px">Phone</div>
  <div class="abs field" style="left:516px;top:3980px;width:561px;height:120px">Message</div>
  <div class="abs btn btn-clay" style="left:516px;top:4127px;width:111px;height:28px">Submit</div>
</section>

<footer class="abs footer">
  <div class="abs" style="left:150px;top:70px;width:160px;text-align:center">
    <div style="width:54px;height:54px;border:2px solid var(--white);margin:0 auto 12px"></div>
    <div style="font-size:24px;font-weight:500;line-height:1">MERIDIAN</div>
    <div style="font-size:9px;letter-spacing:2px">ESCROW SOLUTIONS</div>
  </div>
  <div class="abs" style="left:398px;top:60px"><h4>Quick Links</h4><div class="flinks">Home<br>About Us<br>Services<br>Testimonials<br>Resources</div></div>
  <div class="abs" style="left:539px;top:60px">
    <h4>Contact Info</h4>
    <div class="crow"><i><svg width="12" height="12" viewBox="0 0 12 12" fill="none" stroke="#bf6f58" stroke-width="1.2"><path d="M2 1h2l1 3-1.5 1a6 6 0 003 3L8 7l3 1v2a1 1 0 01-1 1A9 9 0 011 2a1 1 0 011-1z"/></svg></i>+1 555 014 2388</div>
    <div class="crow"><i><svg width="12" height="10" viewBox="0 0 12 10" fill="none" stroke="#bf6f58" stroke-width="1.2"><rect x="1" y="1" width="10" height="8"/><path d="M1 1l5 4 5-4"/></svg></i>contact@meridianescrow.com</div>
    <div class="crow"><i><svg width="10" height="12" viewBox="0 0 10 12" fill="none" stroke="#bf6f58" stroke-width="1.2"><path d="M5 11S1 7 1 4.5a4 4 0 018 0C9 7 5 11 5 11z"/><circle cx="5" cy="4.5" r="1.3"/></svg></i><span>48 Harbor Lane, Suite 210<br>Portland, OR 97201</span></div>
  </div>
  <div class="abs" style="left:809px;top:60px;width:268px">
    <h4>Subscribe Our Newsletter</h4>
    <div style="border:1px solid #8a91a0;border-radius:3px;height:36px;font-size:9px;color:#b8bcc4;padding:12px 16px">Enter your email</div>
    <div class="btn btn-clay" style="height:29px;margin-top:15px">Subscribe Now</div>
  </div>
  <div class="abs" style="left:122px;top:260px;width:955px;height:1px;background:#56607a"></div>
  <div class="abs" style="left:122px;top:278px;display:flex;gap:8px">
    <span style="width:24px;height:24px;border-radius:50%;background:var(--white)"></span>
    <span style="width:24px;height:24px;border-radius:50%;border:1px solid var(--white)"></span>
    <span style="width:24px;height:24px;border-radius:50%;border:1px solid var(--white)"></span>
    <span style="width:24px;height:24px;border-radius:50%;border:1px solid var(--white)"></span>
  </div>
  <p class="abs" style="left:800px;width:277px;text-align:right;top:284px;font-size:10px;color:#d4d7dd">© Copyright All Right Reserved 2024.</p>
</footer>

</body>
</html>
```